Dental Bridgeway Company Needs Design for Table top Display at Tradeshows

We need a Graphic Design for a Table Top Display that is used at Trade-shows we attend.
A little bit about what we do: We are a Dental Transitions company, we help new and retiring dentists buy or sell their dental practices. Think of it as a real-estate broker for Dental businesses. Some of the things that Transitions include are practice valuations, which is a determination of how much that practice is worth in respect the the amount of business that comes through on a yearly basis. We also help dentists find associates, or help new graduates find associateships.
KMV Dental Crossings was founded by Martin L. Okafor, whom is an attorney in the dental field, who brings a new perspective to the dental transition experience due to his legal background.
About the project: We have a table top display called an Voru TK-4 (Spec sheet attatched, but don't worry, the printers will do all the cutting and printing..but this will let you see how the actual display is divided, however, the image should be one cohesive image), it consists of 5 (3 main and two very small side) panels made from vinyl. Here are the approx. specs of the display.
Height: 1.51 m
59.5''
Width: 2.44 m
96''
Depth: 0.52 m
20.4''
Our printers request Vector graphics or EPS, and the color mode must be Pantone / PMS Spot Color
What we would like to see: We need our company logo, motto "We are here to guide you through"
Colors: Deep Burgundy, White, Grey, and Black
A list of our services: Practice Sales, Buyer Representation, Seller Representation, Practice Valuations, Associateships
We need the font to be large and clear, easy to read, because people are going to be walking by this display, you need to be able to read it quick! We are open to creative design Ideas!
View our website to see more about out and our general marketing image: www.okaforclinicguides.example
Please add in www.kmvcrossings.example to the image (this website is not live yet but will be soon)
Our sliders were accidentally incorrect, the design slider was all the way to "feminine" but we need the design to appeal to both men, and women equally. It has been updated. Thank you
Target Market(s)
Our market is largely retiring dentists, and also new dentists looking to start.
Industry/Entity Type
Marketing
Requirements
Must have
- Must have company logo, name, motto, website and list of services.
Services are: Practice Valuations, Practice Sales, Buyer Representation, Seller Representation, Associateships.
Please remake logo into vector format as well to go along with the vector format (but keep it as close to the original as possible)
Should not have
- No teeth please :)

```html
<!DOCTYPE html>
<html lang="en">
<head>
<meta charset="utf-8">
<title>KMV Dental Crossings – Table Top Display</title>
<link rel="stylesheet" href="https://fonts.googleapis.com/css2?family=Cabin:wght@400;500;600;700&display=swap">
<style>
  :root {
    --burgundy: #3a0012;
    --burgundy-deep: #2a000c;
    --panel-grey: #5f5b5a;
    --rule-grey: #b8b8b8;
    --ink: #111111;
    --white: #ffffff;
    --photo-light: #d9d4d2;
    --photo-dark: #3c3436;
  }
  * { margin: 0; padding: 0; box-sizing: border-box; }
  html, body { width: 1200px; height: 998px; overflow: hidden; background: var(--white); }
  body { font-family: "Cabin", "Trebuchet MS", sans-serif; color: var(--ink); }

  .display {
    position: relative;
    width: 1200px;
    height: 998px;
    background: var(--white);
    border-top: 2px solid #333;
    overflow: hidden;
  }

  .brand {
    position: absolute;
    left: 30px;
    top: 70px;
    display: flex;
    align-items: center;
    gap: 22px;
  }
  .brand__mark {
    width: 92px;
    height: 92px;
    background: var(--burgundy);
  }
  .brand__name {
    font-size: 104px;
    font-weight: 700;
    line-height: 1;
    color: var(--burgundy);
    letter-spacing: 1px;
    white-space: nowrap;
  }
  .brand__rule {
    position: absolute;
    left: 330px;
    top: 242px;
    width: 810px;
    height: 6px;
    background: linear-gradient(90deg, var(--rule-grey) 0%, var(--burgundy) 45%, var(--rule-grey) 100%);
  }

  .motto {
    position: absolute;
    right: 55px;
    top: 350px;
    font-size: 32px;
    font-weight: 500;
    color: var(--burgundy);
  }

  .services {
    position: absolute;
    left: 100px;
    top: 425px;
    width: 448px;
    height: 372px;
    background: var(--panel-grey);
    border-radius: 22px;
    color: var(--white);
    padding: 26px 0 0 72px;
  }
  .services__title {
    font-size: 32px;
    font-weight: 400;
    letter-spacing: 7px;
    margin-bottom: 14px;
  }
  .services__list { list-style: none; }
  .services__item {
    position: relative;
    font-size: 32px;
    line-height: 1;
    letter-spacing: 2px;
    margin-bottom: 28px;
  }
  .services__item::before {
    content: "";
    position: absolute;
    left: -50px;
    top: 9px;
    border-left: 12px solid var(--white);
    border-top: 7px solid transparent;
    border-bottom: 7px solid transparent;
  }
  .services__item--wide { letter-spacing: 7px; }

  .team-photo {
    position: absolute;
    left: 695px;
    top: 498px;
    width: 350px;
    height: 342px;
    background: radial-gradient(ellipse at 50% 75%, var(--photo-dark) 0%, #6b6264 45%, var(--photo-light) 75%, var(--white) 100%);
  }

  .footer {
    position: absolute;
    left: 0;
    bottom: 0;
    width: 1200px;
    height: 158px;
    background: var(--burgundy);
    color: var(--white);
  }
  .footer__web {
    position: absolute;
    left: 295px;
    top: 44px;
    font-size: 50px;
    font-weight: 500;
    letter-spacing: 1px;
  }
  .footer__contact {
    position: absolute;
    left: 1003px;
    top: 24px;
    font-size: 13px;
    line-height: 18px;
    font-style: normal;
  }
</style>
</head>
<body>
<main class="display">
  <header>
    <div class="brand">
      <span class="brand__mark"></span>
      <h1 class="brand__name">KMV Dental Crossings</h1>
    </div>
    <div class="brand__rule"></div>
    <p class="motto">We are here to guide you through</p>
  </header>

  <section class="services">
    <h2 class="services__title">Our Services:</h2>
    <ul class="services__list">
      <li class="services__item services__item--wide">Practice Sales</li>
      <li class="services__item">Buyer Representation</li>
      <li class="services__item">Seller Representation</li>
      <li class="services__item">Practice Valuations</li>
      <li class="services__item services__item--wide">Associateships</li>
    </ul>
  </section>

  <div class="team-photo" role="img" aria-label="Photo of the three-person company team standing together in business attire"></div>

  <footer class="footer">
    <p class="footer__web">www.kmvcrossings.example</p>
    <address class="footer__contact">
      42 Linden Row<br>
      Suite C.<br>
      Harlow, NC 28990<br>
      704-555-0187<br>
      704-555-0143 (FAX)<br>
      mokafor@kmvmail.example
    </address>
  </footer>
</main>
</body>
</html>
```